ARC VOLLEY Business Card Project

I'd like to request a business card design for the new company I've launched.
The name of the company is "ARC VOLLEY" an indoor unmanned tennis practice facility.
We would like to see designs that use our brand identity color in the logo I've attached.
We hope to get the design with modern, luxurious and elegant tone and manner.
We hope the logo should not be too big.

Business card must have elements as below:
- Logo (One of the logos I've attached)
- Name (In Korean Text) : 박 서 윤
- Title (In Korean Text) : 대표
- Phone Number : 010-8472-3916
- Email Address : seoyun.park@arcvolley-example.co.kr
- Website : www.arcvolley-example.co.kr
- Instagram : arcvolley
- Address (In Korean text) : 경기도 용인시 수지구 풍덕천로 456 미래타워 5층 501호, 502호

Target Market(s)

Tennis amateurs in 20 to 40s

Industry/Entity Type

Sports, Hobby

Contact Information for Business Card

- Logo (One of the logos I've attached) - Name (In Korean Text) : 박 서 윤 - Title (In Korean Text) : 대표 - Phone Number : 010-8472-3916 - Email Address : seoyun.park@arcvolley-example.co.kr - Website : www.arcvolley-example.co.kr - Instagram : arcvolley - Address (In Korean text) : 경기도 용인시 수지구 풍덕천로 456 미래타워 5층 501호, 502호

Font styles to use
Sans Serif

Requirements
Must have
• Double sided
Nice to have
• Logo with intaglio or relief embossing
Should not have
• Logo should not be too big.

```html
<!DOCTYPE html>
<html lang="ko">
<head>
<meta charset="utf-8">
<title>ARC VOLLEY Business Card</title>
<link href="https://fonts.googleapis.com/css2?family=Noto+Sans+KR:wght@400;500;700&display=swap" rel="stylesheet">
<style>
  :root {
    --bg: #e6e6e6;
    --brand-green: #2e4f38;
    --emboss-green: #3d6147;
    --card-light: #f4f4f4;
    --text-gray: #555555;
    --muted-gray: #666666;
    --watermark: #e3e3e3;
  }
  html, body {
    margin: 0;
    width: 1200px;
    height: 960px;
    overflow: hidden;
    background: var(--bg);
    font-family: "Noto Sans KR", sans-serif;
  }
  .canvas { position: relative; width: 1200px; height: 960px; }
  .card {
    position: absolute;
    left: 302px;
    width: 603px;
    height: 345px;
    overflow: hidden;
  }
  .card-front { top: 111px; background: var(--brand-green); }
  .card-back { top: 509px; background: var(--card-light); }

  .front-mark {
    position: absolute;
    left: 115px;
    top: 136px;
    display: flex;
    align-items: center;
    gap: 16px;
  }
  .front-mark .mark-dot {
    width: 74px; height: 74px; border-radius: 50%;
    background: var(--emboss-green);
  }
  .front-mark .brand-name {
    font-size: 36px; font-weight: 500; letter-spacing: 2px;
    color: var(--emboss-green);
  }

  .back-mark { position: absolute; left: 40px; top: 32px; }
  .back-mark .mark-dot {
    width: 70px; height: 70px; border-radius: 50%;
    background: var(--brand-green);
    margin-left: 61px;
  }
  .back-mark .brand-name {
    margin-top: 16px;
    font-size: 24px; font-weight: 500; letter-spacing: 1px;
    color: var(--brand-green); line-height: 1;
  }

  .watermark-ring {
    position: absolute; left: 340px; top: 140px;
    width: 240px; height: 240px; border-radius: 50%;
    border: 22px solid var(--watermark);
  }

  .person { position: absolute; right: 46px; top: 60px; text-align: right; }
  .person .name {
    font-size: 20px; font-weight: 700; letter-spacing: 3px;
    color: var(--brand-green); line-height: 1.2;
  }
  .person .title { font-size: 14px; color: var(--muted-gray); margin-top: 2px; }

  .contacts {
    position: absolute; left: 40px; top: 178px;
    list-style: none; margin: 0; padding: 0;
    font-size: 14.5px; color: var(--text-gray);
  }
  .contacts li { display: flex; align-items: flex-start; gap: 6px; line-height: 20.5px; }
  .contacts li.address { margin-bottom: 9px; }
  .contacts svg { width: 13px; height: 13px; flex: none; margin-top: 4px; }
</style>
</head>
<body>
<div class="canvas">
  <section class="card card-front" aria-label="Card front">
    <div class="front-mark">
      <span class="mark-dot"></span>
      <span class="brand-name">ARC VOLLEY</span>
    </div>
  </section>

  <section class="card card-back" aria-label="Card back">
    <div class="watermark-ring"></div>

    <div class="back-mark">
      <div class="mark-dot"></div>
      <div class="brand-name">ARC VOLLEY</div>
    </div>

    <div class="person">
      <div class="name">박 서 윤</div>
      <div class="title">대표</div>
    </div>

    <ul class="contacts">
      <li class="address">
        <svg viewBox="0 0 14 14"><path d="M7 1a4.3 4.3 0 0 0-4.3 4.3C2.7 8.6 7 13 7 13s4.3-4.4 4.3-7.7A4.3 4.3 0 0 0 7 1z" fill="none" stroke="#444" stroke-width="1.5"/><circle cx="7" cy="5.3" r="1.5" fill="none" stroke="#444" stroke-width="1.3"/></svg>
        <span>경기도 용인시 수지구 풍덕천로<br>456 미래타워 5층 501호, 502호</span>
      </li>
      <li>
        <svg viewBox="0 0 14 14"><path d="M3 1.5l2.2 2.6-1.2 1.6a7 7 0 0 0 4.3 4.3l1.6-1.2 2.6 2.2-1.2 1.5C7 12.5 1.5 7 1.5 2.7z" fill="none" stroke="#444" stroke-width="1.4" stroke-linejoin="round"/></svg>
        <span>010-8472-3916</span>
      </li>
      <li>
        <svg viewBox="0 0 14 14"><rect x="1.2" y="2.8" width="11.6" height="8.4" rx="1" fill="none" stroke="#444" stroke-width="1.4"/><path d="M1.5 3.5L7 7.8l5.5-4.3" fill="none" stroke="#444" stroke-width="1.4"/></svg>
        <span>seoyun.park@arcvolley-example.co.kr</span>
      </li>
      <li>
        <svg viewBox="0 0 14 14"><circle cx="7" cy="7" r="5.8" fill="none" stroke="#444" stroke-width="1.3"/><ellipse cx="7" cy="7" rx="2.5" ry="5.8" fill="none" stroke="#444" stroke-width="1.1"/><path d="M1.2 7h11.6" stroke="#444" stroke-width="1.1"/></svg>
        <span>www.arcvolley-example.co.kr</span>
      </li>
      <li>
        <svg viewBox="0 0 14 14"><rect x="1.5" y="1.5" width="11" height="11" rx="2.5" fill="none" stroke="#444" stroke-width="1.5"/></svg>
        <span>@arcvolley</span>
      </li>
    </ul>
  </section>
</div>
</body>
</html>
```